Update our business cards to match our awesome new website

Need a new design for company business cards. We have recently revamped our website and would like our business cards to get a refresh too. I've uploaded the company artwork, logo, as well as the Branding Deck to better understand the look & feel of our brand. Please visit the website at hollowbrookestatesmi.com.

Industry/Entity Type

Real Estate

Contact Information for Business Card

must use the colors outlined in the Branding Deck uploaded to the site, or the colors of our logo.

Font styles to use
Other font styles liked:
• Calibri

Requirements
Must have
• Required items: Name, title, company logo, address: 218 Fenwick St. Suite 300, Northville, MI 48173, email address: cole@hollowbrookestatesMI.com, company phone 800-555-0193, cell: 248-555-0162
Nice to have
• a more simple design. not complicated
Should not have
• cartoonish characters, or whimsical writing or artwork, stay within our branding colors

```html
<!DOCTYPE html>
<html lang="en">
<head>
<meta charset="utf-8">
<title>Hollowbrook Estates – Business Cards</title>
<link rel="stylesheet" href="https://fonts.googleapis.com/css2?family=Poppins:wght@400;500&display=swap">
<style>
  :root {
    --stage: #26272a;
    --paper: #ffffff;
    --ink: #1d1d1f;
    --brand-blue: #1373c0;
    --brand-green: #17a673;
    --photo-deep: #123848;
    --photo-mid: #1f5f78;
    --photo-light: #7b9aa6;
    --band-glass: rgba(40, 60, 70, 0.55);
  }
  * { box-sizing: border-box; margin: 0; padding: 0; }
  html, body { width: 1200px; height: 1200px; overflow: hidden; }
  body {
    background: var(--stage);
    font-family: "Poppins", Arial, sans-serif;
    display: flex;
    flex-direction: column;
    align-items: center;
    justify-content: center;
    gap: 56px;
  }
  .card {
    position: relative;
    width: 900px;
    height: 514px;
    background: var(--paper);
    overflow: hidden;
    box-shadow: 0 10px 30px rgba(0,0,0,0.45);
  }

  /* Front */
  .front-photo {
    position: absolute;
    left: 0; top: 150px; right: 0; bottom: 0;
    background: linear-gradient(120deg, var(--photo-mid) 0%, var(--photo-deep) 55%, #0f2c38 100%);
  }
  .front-photo::after {
    content: "";
    position: absolute;
    left: 200px; top: 60px; width: 560px; bottom: 0;
    background: radial-gradient(ellipse at center, rgba(190,170,160,0.35), transparent 70%);
  }
  .front-wave { position: absolute; left: 0; top: 0; width: 900px; height: 320px; }
  .front-logo {
    position: absolute;
    left: 0; right: 0; top: 72px;
    text-align: center;
    padding-left: 120px;
  }
  .web-band {
    position: absolute;
    left: 0; right: 0; top: 420px; height: 52px;
    background: var(--band-glass);
    display: flex; align-items: center;
    padding-left: 290px;
    color: var(--paper);
    font-size: 24px;
    letter-spacing: 0.5px;
  }

  /* Logo name */
  .brand-name {
    color: var(--ink);
    font-weight: 500;
    text-transform: uppercase;
    letter-spacing: 1px;
    line-height: 1;
    font-size: 36px;
  }
  .brand-sub {
    display: block;
    color: var(--ink);
    font-weight: 500;
    font-size: 13px;
    text-align: right;
    margin-top: 6px;
    letter-spacing: 0.5px;
  }
  .brand { display: inline-block; }

  /* Back */
  .back-logo { position: absolute; left: 50px; top: 190px; }
  .back-logo .brand-name { font-size: 31px; }
  .divider {
    position: absolute; left: 470px; top: 150px;
    width: 2px; height: 170px; background: var(--ink);
  }
  .contact { position: absolute; left: 505px; top: 150px; color: var(--ink); }
  .person-name { font-size: 30px; font-weight: 400; text-transform: uppercase; letter-spacing: 1px; line-height: 1.05; }
  .person-title { color: var(--brand-green); font-size: 20px; margin-bottom: 14px; }
  .contact-row { display: flex; align-items: center; gap: 12px; font-size: 21px; line-height: 1.5; }
  .contact-row svg { width: 18px; height: 18px; flex: none; }
  .address-band {
    position: absolute; left: 0; right: 0; top: 400px; height: 54px;
    background: var(--brand-blue);
    color: var(--paper);
    font-size: 23px;
    display: flex; align-items: center;
    padding-left: 230px;
  }
  .address-band::before {
    content: ""; position: absolute; left: 0; right: 0; top: 0; height: 4px;
    background: var(--brand-blue); opacity: 0.6;
  }
</style>
</head>
<body>

  <section class="card card-front">
    <div class="front-photo" role="img" aria-label="Photo of a happy multi-generation family gathered in a teal-walled living room"></div>
    <svg class="front-wave" viewBox="0 0 900 320" aria-hidden="true">
      <path d="M0 0 H900 V165 C760 168 650 235 460 222 C380 215 330 175 300 150 H0 Z" fill="var(--paper)"/>
    </svg>
    <div class="front-logo">
      <span class="brand">
        <span class="brand-name">Hollowbrook Estates</span>
        <span class="brand-sub">of Michigan, LLC</span>
      </span>
    </div>
    <div class="web-band">hollowbrookestatesmi.com</div>
  </section>

  <section class="card card-back">
    <div class="back-logo">
      <span class="brand">
        <span class="brand-name">Hollowbrook Estates</span>
        <span class="brand-sub">of Michigan, LLC</span>
      </span>
    </div>
    <div class="divider"></div>
    <div class="contact">
      <div class="person-name">Cole Avery</div>
      <div class="person-title">Manager</div>
      <div class="contact-row">
        <svg viewBox="0 0 24 24" aria-hidden="true"><path d="M6.6 10.8a15.1 15.1 0 0 0 6.6 6.6l2.2-2.2a1 1 0 0 1 1-.25 11.4 11.4 0 0 0 3.6.57 1 1 0 0 1 1 1V20a1 1 0 0 1-1 1A17 17 0 0 1 3 4a1 1 0 0 1 1-1h3.5a1 1 0 0 1 1 1c0 1.25.2 2.45.57 3.57a1 1 0 0 1-.25 1z" fill="var(--brand-blue)"/></svg>
        <span>800-555-0193</span>
      </div>
      <div class="contact-row">
        <svg viewBox="0 0 24 24" aria-hidden="true"><rect x="6" y="2" width="12" height="20" rx="2" fill="none" stroke="var(--brand-blue)" stroke-width="2.2"/></svg>
        <span>248-555-0162</span>
      </div>
      <div class="contact-row">
        <svg viewBox="0 0 24 24" aria-hidden="true"><rect x="2" y="5" width="20" height="14" fill="var(--brand-blue)"/><path d="M2 5 L12 13 L22 5" fill="none" stroke="var(--paper)" stroke-width="1.6"/></svg>
        <span>cole@hollowbrookestatesMI.com</span>
      </div>
    </div>
    <div class="address-band">218 Fenwick St. Suite 300, Northville, MI 48173</div>
  </section>

</body>
</html>
```